Savings/Retirement Infographic

I need an infographic to convey the importance of retirement planning and saving regularly. It must be an attractive and compelling design that people want to read.

The design will primarily be used as a poster, but also as an emailer and a shorter version for an A5 flyer.

Content:

There are only two types of retirement funds
Big or Small

Big retirement funds = Foreign Travel,
Sailing,
Concerts,
Sky Diving,
Fishing,
Golf,
Fine Dining,
Spoiling Grandchildren,
Sandy Beaches.

Small retirement funds = Counting every penny,
Sitting at home,
Relying on family, friends and charity,
Turning off the heating in Winter

Big pensions are acquired over the length of a career with careful planning and motivation.

Small pensions take no effort at all.

Which are you aiming for?

Did you know?
1 in 5 people retiring in 2013 will be below the poverty line?
In the UK, 14% will rely solely on a state pension. That's less than AED 640 per week.
(Source: Harrowgate Cohort of 2013)

Of 100 people aged 25 today, by age 65
1 will be wealthy
4 will be financially independent
5 will still be working
12 will be bankrupt
29 will already be dead
49 will be dependent on others

Of those still living, 86% will rely on friends, relatives and charity.

To retire on $30,000 per annum, you'll need approx.. $600,000 in today's terms.
That's $1,456,380 in 30 years with 3% inflation.
By saving in a bank earning ZERO interest, you need to save $4,045 each month for 30 years
If you invest in the markets and earn 5% interest each year, you only need to save $2,307 each month.
If you manage to get 10% per annum interest, you'll only need to save $934 per month. That's less than AED 3,450.

Please add a bar across the bottom with my contact details, leaving space for my photo and logo. Contact details:

E: rmoss@tidalnest.com
M: 050 8126 473

```html
<!DOCTYPE html>
<html lang="en">
<head>
<meta charset="utf-8">
<title>Savings for Retirement</title>
<link href="https://fonts.googleapis.com/css2?family=Bowlby+One&family=Oswald:wght@500;700&family=Roboto:ital,wght@0,400;0,700;1,400&display=swap" rel="stylesheet">
<style>
:root{
  --teal:#17aaa8;
  --navy:#22506d;
  --orange:#f07a24;
  --orange-dark:#b9561a;
  --sky:#7aa7c1;
  --sky-dark:#4f7f9b;
  --panel:#ececec;
  --rule:#b9b9b9;
  --ink:#222222;
  --white:#ffffff;
}
*{margin:0;padding:0;box-sizing:border-box}
html,body{width:849px;height:1200px;overflow:hidden;background:var(--white)}
.poster{position:relative;width:849px;height:1200px;overflow:hidden;background:var(--white);font-family:"Roboto",Arial,sans-serif;color:var(--navy)}
.abs{position:absolute;white-space:nowrap}
.art{position:absolute;border-radius:10px}

.hero-pig{left:35px;top:30px;width:215px;height:165px;border-radius:50% 45% 45% 50%;background:var(--navy)}
.title{left:262px;top:34px;font-family:"Bowlby One",sans-serif;font-size:68px;line-height:74px;color:var(--teal);font-weight:400}
.subtitle{left:258px;top:194px;font-size:16.5px;line-height:26px}
.subtitle b{font-size:25px;margin-left:10px;vertical-align:-2px}

.banner{top:237px;height:46px;font-family:"Oswald",sans-serif;font-weight:500;font-size:23px;color:var(--white);line-height:46px}
.banner-big{left:0;width:318px;background:var(--orange);padding-left:40px}
.banner-small{left:530px;width:319px;background:var(--sky);padding-left:18px}
.fold{top:264px;width:24px;height:34px}
.fold-big{left:304px;background:var(--orange-dark);clip-path:polygon(0 0,100% 30%,100% 100%,0 100%)}
.fold-small{left:519px;background:var(--sky-dark);clip-path:polygon(0 30%,100% 0,100% 100%,0 100%)}

.icons-big{left:30px;top:292px;width:262px;height:74px;background:linear-gradient(90deg,var(--orange),#f39a52)}
.icons-small{left:556px;top:298px;width:256px;height:66px;background:var(--sky-dark)}
.money-bags{left:365px;top:262px;width:120px;height:96px;border-radius:40% 40% 30% 30%;background:linear-gradient(90deg,var(--orange) 55%,var(--navy) 55%)}

.copy{font-size:14.5px;line-height:18px;color:var(--ink)}
.list-big{left:40px;top:375px}
.list-small{left:541px;top:372px}
.note-big{left:40px;top:448px}
.note-small{left:676px;top:475px}
.calendar{left:220px;top:440px;width:52px;height:52px;border:5px solid var(--orange);border-top-width:12px;border-radius:6px;font-family:"Oswald",sans-serif;font-size:24px;font-weight:700;color:var(--orange);text-align:center;line-height:32px;background:var(--white)}
.sitter{left:604px;top:447px;width:56px;height:66px;background:var(--navy)}

.aim{left:300px;top:378px;width:240px;text-align:center;font-family:"Bowlby One",sans-serif;font-size:28px;line-height:41px;color:var(--navy)}

.teal-base{left:0;top:770px;width:849px;height:430px;background:var(--teal)}
.panel{left:37px;top:542px;width:775px;height:490px;border-radius:26px;background:var(--panel)}
.ribbon{left:265px;top:522px;width:320px;height:46px;background:var(--teal);color:var(--white);font-family:"Bowlby One",sans-serif;font-weight:400;font-size:24px;text-align:center;line-height:46px;clip-path:polygon(0 0,100% 0,96% 50%,100% 100%,0 100%,4% 50%)}

.people{left:57px;top:580px;width:140px;height:52px;background:linear-gradient(90deg,var(--sky-dark) 80%,var(--orange) 80%)}
.stat-head{font-weight:700;font-size:15px;line-height:19px;color:var(--ink)}
.poverty{left:210px;top:594px}
.big-pct{font-family:"Oswald",sans-serif;font-weight:700;color:var(--orange);line-height:1}
.pct-14{left:57px;top:654px;font-size:68px}
.state{left:210px;top:662px;font-size:14.5px;line-height:18px;color:var(--ink)}
.source{left:210px;top:723px;font-size:11px;line-height:14px;font-style:italic;color:var(--ink)}
.rule-h{height:1px;background:var(--rule)}
.rule-left{left:60px;top:750px;width:370px}
.rule-v{left:455px;top:592px;width:1px;height:410px;background:var(--rule)}

.cohort-head{left:60px;top:762px;font-weight:700;font-size:17px;line-height:22px;color:var(--sky-dark)}
.donut{left:38px;top:805px}
.cohort-list{left:196px;top:794px;list-style:none;font-weight:700;font-size:14.5px;line-height:24px;color:var(--ink)}
.cohort-list span{display:inline-block;width:22px}
.pct-86{left:80px;top:950px;font-size:36px;color:var(--sky-dark)}
.hand{left:68px;top:996px;width:90px;height:28px;background:var(--orange)}
.rely{left:196px;top:966px;font-size:14.5px;line-height:18px;color:var(--ink)}

.need{left:478px;top:588px;font-family:"Oswald",sans-serif;font-weight:700;font-size:34px;line-height:40px;color:var(--orange)}
.need .gt{color:var(--navy);font-size:36px;margin:0 4px}
.need .target{color:var(--sky-dark)}
.need-copy{left:478px;top:634px;font-size:14.5px;line-height:18px;color:var(--ink)}
.future{left:478px;top:682px;font-family:"Oswald",sans-serif;font-weight:700;font-size:44px;line-height:50px;color:var(--navy)}
.future-copy{left:478px;top:734px;font-size:14.5px;line-height:18px;color:var(--ink)}
.yrs{left:664px;top:738px;font-family:"Oswald",sans-serif;font-weight:700;font-size:26px;line-height:32px;color:var(--orange)}
.arrow-up{left:740px;top:694px}

.pig-zero{left:462px;top:800px;width:92px;height:80px;border-radius:50%;background:var(--orange);color:var(--white);font-family:"Oswald",sans-serif;font-weight:700;font-size:38px;text-align:center;line-height:80px}
.monthly{left:568px;top:790px;font-family:"Oswald",sans-serif;font-weight:700;font-size:30px;line-height:36px;color:var(--navy)}
.monthly-copy{left:568px;top:834px;font-size:14.5px;line-height:18px;color:var(--ink)}
.rule-right{left:470px;top:902px;width:230px}
.pct-5{left:470px;top:930px;font-size:36px}
.chart{left:545px;top:912px}
.market-copy{left:470px;top:990px;font-size:14.5px;line-height:18px;color:var(--ink)}
.pct-10{left:640px;top:930px;font-size:36px}
.pig-934{left:718px;top:900px;width:88px;height:66px;border-radius:50%;background:var(--navy);color:var(--white);font-family:"Oswald",sans-serif;font-weight:700;font-size:24px;text-align:center;line-height:70px}
.ten-copy{left:640px;top:983px;font-size:14.5px;line-height:18px;color:var(--ink)}

.brand{left:36px;top:1066px;display:flex;flex-direction:column;gap:8px}
.brand-mark{width:52px;height:52px;background:var(--white)}
.brand-name{font-family:"Oswald",sans-serif;font-weight:700;font-size:26px;color:var(--white);letter-spacing:1px}
.photo{left:326px;top:1036px;width:106px;height:126px;border:5px solid var(--navy);border-radius:16px;background:linear-gradient(#d9dde0,#8f9aa3)}
.advisor{left:446px;top:1084px;font-family:"Oswald",sans-serif;font-weight:700;color:var(--white);line-height:1}
.advisor .first{font-size:20px;display:block;letter-spacing:1px}
.advisor .last{font-size:46px;display:block}
.rule-contact{left:567px;top:1108px;width:2px;height:62px;background:var(--white)}
.contact{left:580px;color:var(--white);font-weight:700;line-height:1}
.email{top:1118px;font-size:19px}
.mobile{top:1146px;font-size:25px}
</style>
</head>
<body>
<main class="poster">
  <div class="art hero-pig" role="img" aria-label="Piggy bank filled with dollar signs"></div>
  <h1 class="abs title">SAVINGS FOR<br>RETIREMENT</h1>
  <p class="abs subtitle">There are only two types of retirement funds <b>BIG or SMALL</b></p>

  <div class="abs fold fold-big"></div>
  <h2 class="abs banner banner-big">Big Retirement Funds</h2>
  <div class="abs fold fold-small"></div>
  <h2 class="abs banner banner-small">Small Retirement Funds</h2>

  <div class="art icons-big" role="img" aria-label="Icons of travel, beach holiday and golf"></div>
  <div class="art money-bags" role="img" aria-label="Large and small money bags"></div>
  <div class="art icons-small" role="img" aria-label="Icons of calculator, heating switched off and family at a table"></div>

  <p class="abs copy list-big">Foreign Travel, Sailing, Concerts,<br>Sky Diving, Fishing, Golf, Fine Dining,<br>Spoiling Grandchildren, Sandy Beaches.</p>
  <p class="abs copy note-big">Big pensions are<br>acquired over the length<br>of a career with careful<br>planning and motivation.</p>
  <div class="abs calendar">12</div>

  <p class="abs aim">WHICH<br>ARE YOU<br>AIMING FOR?</p>

  <p class="abs copy list-small">Counting every penny, Sitting at home,<br>Relying on family, &nbsp;friends and charity,<br>Turning off the heating in Winter</p>
  <div class="art sitter" role="img" aria-label="Elderly person sitting with a cane"></div>
  <p class="abs copy note-small">Small pensions<br>take no effort at all.</p>

  <div class="abs teal-base"></div>
  <section class="abs panel"></section>
  <h2 class="abs ribbon">DID YOU KNOW?</h2>

  <div class="art people" role="img" aria-label="Five people, one highlighted"></div>
  <p class="abs stat-head poverty">1 in 5 people retiring in 2013<br>will be below the poverty line?</p>
  <p class="abs big-pct pct-14">14%</p>
  <p class="abs state">In the UK, 14% will rely solely on<br>a state pension. That's less than<br>AED 640 per week.</p>
  <p class="abs source">(Source: Harrowgate Cohort of 2013)</p>
  <div class="abs rule-h rule-left"></div>
  <div class="abs rule-v"></div>

  <h3 class="abs cohort-head">Of 100 people aged 25 today, by age 65</h3>
  <svg class="abs donut" width="124" height="124" viewBox="-62 -62 124 124" aria-label="Pie chart of 100 people">
    <circle r="45" fill="none" stroke="#fbdcc3" stroke-width="34"/>
    <circle r="45" fill="none" stroke="#f6a468" stroke-width="34" stroke-dasharray="138.5 144.3" transform="rotate(-90)"/>
    <circle r="45" fill="none" stroke="#f6b583" stroke-width="34" stroke-dasharray="0 138.5 82 200" transform="rotate(-90)"/>
    <circle r="28" fill="#ffffff"/>
    <text y="8" text-anchor="middle" font-family="Oswald, sans-serif" font-weight="700" font-size="22" fill="#f07a24">100</text>
  </svg>
  <ul class="abs cohort-list">
    <li><span>01</span> will be wealthy</li>
    <li><span>04</span> will be financially independent</li>
    <li><span>05</span> will still be working</li>
    <li><span>12</span> will be bankrupt</li>
    <li><span>29</span> will already be dead</li>
    <li><span>49</span> will be dependent on others</li>
  </ul>
  <p class="abs big-pct pct-86">86%</p>
  <div class="art hand" role="img" aria-label="Open helping hand"></div>
  <p class="abs rely">Of those still living, 86% will rely<br>on friends, relatives and charity.</p>

  <p class="abs need">$30,000<span class="gt">&gt;</span><span class="target">$600,000</span></p>
  <p class="abs need-copy">To retire on $30,000 per annum, you'll need<br>approx.. $600,000 in today's terms.</p>
  <p class="abs future">$1,456,380</p>
  <p class="abs future-copy">That's $1,456,380 in 30<br>years with 3% inflation.</p>
  <p class="abs yrs">30Yrs</p>
  <svg class="abs arrow-up" width="74" height="80" viewBox="0 0 74 80" aria-label="3% rising">
    <polygon points="37,0 74,34 56,34 56,80 18,80 18,34 0,34" fill="#f07a24"/>
    <text x="37" y="70" text-anchor="middle" font-family="Oswald, sans-serif" font-weight="700" font-size="26" fill="#ffffff">3%</text>
  </svg>

  <div class="abs pig-zero" role="img" aria-label="Piggy bank showing zero dollars">$0</div>
  <p class="abs monthly">$4,045 x 30yrs</p>
  <p class="abs monthly-copy">By saving in a bank earning<br>ZERO interest, you need to save<br><b>$4,045</b> each month for <b>30</b> years</p>
  <div class="abs rule-h rule-right"></div>

  <p class="abs big-pct pct-5">5%</p>
  <svg class="abs chart" width="70" height="72" viewBox="0 0 70 72" aria-label="Rising bar chart">
    <rect x="4" y="44" width="10" height="26" fill="#4f7f9b"/>
    <rect x="20" y="36" width="10" height="34" fill="#4f7f9b"/>
    <rect x="36" y="40" width="10" height="30" fill="#4f7f9b"/>
    <rect x="52" y="28" width="10" height="42" fill="#4f7f9b"/>
    <polyline points="2,36 20,22 36,30 60,6" fill="none" stroke="#22506d" stroke-width="4"/>
    <polygon points="52,4 66,0 62,14" fill="#22506d"/>
  </svg>
  <p class="abs market-copy">If you invest in the<br>markets and earn <b>5%</b><br>interest each year,<br>you only need to save<br><b>$2,307</b> each month.</p>
  <p class="abs big-pct pct-10">10%</p>
  <div class="abs pig-934" role="img" aria-label="Piggy bank showing $934">$934</div>
  <p class="abs ten-copy">If you manage to<br>get <b>10%</b> per annum<br>interest, you'll only<br>need to <b>save $934</b><br>per month. That's<br>less than <b>AED 3,450.</b></p>

  <footer>
    <div class="abs brand">
      <div class="brand-mark"></div>
      <span class="brand-name">TIDALNEST</span>
    </div>
    <div class="abs photo" role="img" aria-label="Portrait photo of the adviser"></div>
    <p class="abs advisor"><span class="first">RYAN</span><span class="last">MOSS</span></p>
    <div class="abs rule-contact"></div>
    <p class="abs contact email">E: rmoss@tidalnest.com</p>
    <p class="abs contact mobile">M: 050 8126 473</p>
  </footer>
</main>
</body>
</html>
```